Designs of screens for job search mobile app

Design the following screens:

1. Login
2. Job search results in tabs
3. Job details in cards format
4. Profile
5. Settings

Logo and references are provided. The app need to be playful, easy to use, different from traditional job search app like Workvane, ProLattice and others and targeted to Millennial users (age 18-30).

The main app reference is Piqto, in terms of the colorful and fun color and font scheme.

Target Market(s)

Millennial users (age 18-30).

Requirements
Must have
• A fun, playful feel

```html
<!DOCTYPE html>
<html lang="en">
<head>
<meta charset="utf-8">
<title>Job Search – Search Results</title>
<link rel="stylesheet" href="https://fonts.googleapis.com/css2?family=Oswald:wght@300;400;500&family=Roboto:wght@400;500&display=swap">
<style>
  :root {
    --bg: #a01dd6;
    --grad-start: #9b3fe0;
    --grad-end: #5aa0e0;
    --screen: #f1f1f3;
    --card: #ffffff;
    --ink: #2b2b2b;
    --ink-soft: #555555;
    --accent: #4a74e0;
    --muted: #c9c9cf;
    --logo-ink: #6b2a1a;
  }
  * { box-sizing: border-box; margin: 0; padding: 0; }
  html, body { width: 1200px; height: 864px; overflow: hidden; }
  body {
    background: var(--bg);
    font-family: "Oswald", sans-serif;
    color: var(--ink);
    position: relative;
  }
  .screen {
    position: absolute;
    left: 390px; top: 32px;
    width: 420px; height: 800px;
    background: var(--screen);
    overflow: hidden;
    box-shadow: 0 24px 60px rgba(50, 0, 90, .45);
  }
  .app-header {
    height: 86px;
    background: linear-gradient(90deg, var(--grad-start), var(--grad-end));
    color: #fff;
    position: relative;
  }
  .status-bar {
    height: 22px;
    display: flex; align-items: center; justify-content: space-between;
    padding: 0 10px;
    font-family: "Roboto", sans-serif;
    font-size: 12px;
  }
  .status-bar .carrier { display: flex; align-items: center; gap: 4px; }
  .signal { letter-spacing: -1px; font-size: 10px; }
  .status-bar .right { display: flex; align-items: center; gap: 4px; }
  .battery { width: 22px; height: 10px; border: 1px solid #fff; border-radius: 2px; padding: 1px; }
  .battery span { display: block; width: 77%; height: 100%; background: #fff; }
  .app-title {
    text-align: center;
    font-weight: 300;
    font-size: 20px;
    letter-spacing: 1px;
    margin-top: 12px;
  }
  .filter-btn { position: absolute; left: 16px; top: 44px; }
  .job-list { padding: 14px 14px 0; display: flex; flex-direction: column; gap: 12px; }
  .job-card {
    height: 104px;
    background: var(--card);
    display: grid;
    grid-template-columns: 118px 1fr 86px;
    align-items: center;
    box-shadow: 0 4px 10px rgba(0,0,0,.06);
  }
  .company {
    display: flex; align-items: center; justify-content: center; gap: 5px;
    font-weight: 400; font-size: 15px; color: var(--logo-ink);
  }
  .company .mark { width: 10px; height: 10px; border-radius: 50%; background: currentColor; }
  .company.stridewell { color: #111; }
  .company.packorra { color: #8b1a1a; }
  .company.velaris { color: #22407a; }
  .job-title { font-weight: 300; font-size: 20px; text-transform: uppercase; line-height: 1.15; }
  .job-meta { font-family: "Oswald", sans-serif; font-weight: 300; font-size: 11px; color: var(--ink-soft); line-height: 1.35; margin-top: 3px; }
  .job-meta .salary { font-weight: 400; color: var(--ink); }
  .job-aside { display: flex; flex-direction: column; align-items: flex-end; padding-right: 14px; gap: 6px; color: var(--accent); font-weight: 300; font-size: 12px; }
  .tab-bar {
    position: absolute; left: 0; bottom: 0; width: 100%; height: 84px;
    background: #fff;
    display: flex; align-items: center; justify-content: space-around;
  }
  .tab { width: 60px; height: 84px; display: flex; align-items: center; justify-content: center; position: relative; }
  .tab.active::after { content: ""; position: absolute; bottom: 0; left: 0; right: 0; height: 3px; background: var(--accent); }
  .fab {
    width: 70px; height: 70px; border-radius: 50%;
    background: linear-gradient(90deg, var(--grad-start), var(--grad-end));
    display: flex; align-items: center; justify-content: center;
    margin-top: -46px;
    box-shadow: 0 6px 14px rgba(80, 60, 200, .35);
  }
</style>
</head>
<body>
  <main class="screen">
    <header class="app-header">
      <div class="status-bar">
        <div class="carrier"><span class="signal">●●●○○</span> Nettra
          <svg width="12" height="9" viewBox="0 0 12 9"><path d="M1 3a7 7 0 0 1 10 0M3 5a4 4 0 0 1 6 0" fill="none" stroke="#fff" stroke-width="1.3"/><circle cx="6" cy="7.5" r="1.1" fill="#fff"/></svg>
        </div>
        <div class="time">1:23 AM</div>
        <div class="right">77% <div class="battery"><span></span></div></div>
      </div>
      <svg class="filter-btn" width="18" height="16" viewBox="0 0 18 16"><path d="M1 1h16l-6 7v6l-4 2V8z" fill="#fff"/></svg>
      <h1 class="app-title">SEARCH</h1>
    </header>

    <section class="job-list">
      <article class="job-card">
        <div class="company"><span class="mark"></span>Maple Bean</div>
        <div><h2 class="job-title">Software Engineers</h2>
          <p class="job-meta">Singapore<br><span class="salary">$80k - $90k per annum</span><br>3 friends work/worked here</p></div>
        <div class="job-aside"><svg width="24" height="14" viewBox="0 0 24 14"><path d="M1 13L22 2M12 1h10v9" fill="none" stroke="currentColor" stroke-width="1.6"/></svg>43 minutes ago</div>
      </article>
      <article class="job-card">
        <div class="company stridewell"><span class="mark"></span>Stridewell</div>
        <div><h2 class="job-title">Java Developer</h2>
          <p class="job-meta">Manchester<br><span class="salary">$110k - $150k per annum</span><br>2 friends work/worked here</p></div>
        <div class="job-aside"><svg width="24" height="14" viewBox="0 0 24 14"><path d="M1 13L22 2M12 1h10v9" fill="none" stroke="currentColor" stroke-width="1.6"/></svg>7 days ago</div>
      </article>
      <article class="job-card">
        <div class="company packorra"><span class="mark"></span>Packorra</div>
        <div><h2 class="job-title">System Architect</h2>
          <p class="job-meta">Tokyo<br><span class="salary">$100k - $120k per annum</span><br>2 friends work/worked here</p></div>
        <div class="job-aside"><svg width="24" height="14" viewBox="0 0 24 14"><path d="M1 13L22 2M12 1h10v9" fill="none" stroke="currentColor" stroke-width="1.6"/></svg>11 days ago</div>
      </article>
      <article class="job-card">
        <div class="company velaris"><span class="mark"></span>Velaris</div>
        <div><h2 class="job-title">UI/UX Designer</h2>
          <p class="job-meta">Berlin<br><span class="salary">$80k - $90k per annum</span><br>0 friends work/worked here</p></div>
        <div class="job-aside"><svg width="24" height="14" viewBox="0 0 24 14"><path d="M1 13L22 2M12 1h10v9" fill="none" stroke="currentColor" stroke-width="1.6"/></svg>14 days ago</div>
      </article>
      <article class="job-card">
        <div class="company"><span class="mark"></span>Maple Bean</div>
        <div><h2 class="job-title">Branch Manager</h2>
          <p class="job-meta">Valencia<br><span class="salary">$120k - $160k per annum</span><br>4 friends work/worked here</p></div>
        <div class="job-aside"><svg width="24" height="14" viewBox="0 0 24 14"><path d="M1 13L22 2M12 1h10v9" fill="none" stroke="currentColor" stroke-width="1.6"/></svg>17 days ago</div>
      </article>
    </section>

    <nav class="tab-bar">
      <div class="tab active"><svg width="22" height="22" viewBox="0 0 22 22"><circle cx="9" cy="9" r="6.5" fill="none" stroke="#c9c9cf" stroke-width="2.2"/><path d="M14 14l6 6" stroke="#c9c9cf" stroke-width="2.6"/></svg></div>
      <div class="tab"><svg width="24" height="20" viewBox="0 0 24 20"><rect x="1" y="5" width="22" height="14" rx="2" fill="#c9c9cf"/><path d="M8 5V2h8v3" fill="none" stroke="#c9c9cf" stroke-width="2"/></svg></div>
      <div class="fab"><svg width="22" height="20" viewBox="0 0 22 20"><path d="M11 1L1 10h3v9h5v-6h4v6h5v-9h3z" fill="#fff"/></svg></div>
      <div class="tab"><svg width="24" height="20" viewBox="0 0 24 20"><rect x="1" y="1" width="22" height="18" fill="none" stroke="#c9c9cf" stroke-width="1.6"/><path d="M5 6h14M5 10h14M5 14h10" stroke="#c9c9cf" stroke-width="1.4"/></svg></div>
      <div class="tab"><svg width="22" height="22" viewBox="0 0 22 22"><circle cx="11" cy="11" r="6" fill="none" stroke="#c9c9cf" stroke-width="4" stroke-dasharray="3 2.2"/><circle cx="11" cy="11" r="5" fill="#c9c9cf"/><circle cx="11" cy="11" r="2" fill="#fff"/></svg></div>
    </nav>
  </main>
</body>
</html>
```